Cosmetic injections clinic needs a fresh looking business card

We need a business card using the supplied logo and color scheme to attract future clients to our clinic. It should be modern and fresh, eye catching and not too busy. Simple and to the point is best. I would like two sided designs with the front indicating address and contact information, and the back in full color with white logo and descriptive information also provided.
Target Market(s)
Clients looking for non surgical beauty enhancements.
Contact Information for Business Card
Lumivela
14, 415 Carrow Ridge Road
Marrowfield, Northvale
K2P 7W3
Phone: 431-662-0974
Email: info@lumivela-example.com
Requirements
Must have
- -Logo supplied with the name and address of the clinic
- -Back of card in full color with white logo with A small line of text indicating both of the following: Anti aging consultants and cosmetic injectables
- Located inside the Wayfarer Care Group

```html
<!DOCTYPE html>
<html lang="en">
<head>
<meta charset="utf-8">
<title>Lumivela Business Card</title>
<link rel="stylesheet" href="https://fonts.googleapis.com/css2?family=Quicksand:wght@500;700&display=swap">
<style>
  :root {
    --backdrop: #e89cc4;
    --purple: #6a3fa0;
    --purple-deep: #5a3490;
    --purple-light: #7b4fb0;
    --pink: #e5489f;
    --teal: #2bb79a;
    --ink: #2a2a2a;
    --white: #ffffff;
  }
  * { box-sizing: border-box; margin: 0; padding: 0; }
  html, body { width: 1200px; height: 1000px; overflow: hidden; }
  body {
    background: var(--backdrop);
    font-family: "Quicksand", sans-serif;
    position: relative;
  }
  .card {
    position: absolute;
    width: 525px;
    height: 300px;
    border-radius: 30px;
    overflow: hidden;
    box-shadow: 0 10px 30px rgba(90, 40, 80, 0.18);
  }
  .brand-dot {
    width: 20px; height: 20px;
    border-radius: 50%;
    background: var(--pink);
    flex: none;
  }

  /* Front */
  .card-front {
    left: 50px;
    top: 350px;
    background: var(--white);
  }
  .front-brand {
    position: absolute;
    left: 34px;
    top: 130px;
    display: flex;
    align-items: center;
    gap: 9px;
  }
  .front-brand .brand-name {
    font-size: 32px;
    font-weight: 700;
    color: var(--purple);
    letter-spacing: 0.3px;
  }
  .divider {
    position: absolute;
    left: 220px;
    top: 60px;
    width: 2px;
    height: 180px;
    background: linear-gradient(var(--purple), var(--teal) 50%, var(--pink));
  }
  .contact-block {
    position: absolute;
    left: 238px;
    top: 62px;
    right: 20px;
    color: var(--ink);
  }
  .person-name {
    font-size: 18px;
    font-weight: 700;
    color: var(--purple);
    white-space: nowrap;
  }
  .person-title {
    font-size: 12.5px;
    font-weight: 500;
    letter-spacing: 0.6px;
    margin-bottom: 8px;
    white-space: nowrap;
  }
  .contact-row {
    display: flex;
    align-items: flex-start;
    gap: 9px;
    font-size: 14px;
    font-weight: 500;
    line-height: 20px;
    white-space: nowrap;
  }
  .contact-row svg { flex: none; margin-top: 3px; }

  /* Back */
  .card-back {
    left: 625px;
    top: 350px;
    background: linear-gradient(160deg, var(--purple-light), var(--purple-deep));
    color: var(--white);
  }
  .back-brand {
    position: absolute;
    left: 0; right: 0;
    top: 95px;
    display: flex;
    justify-content: center;
    align-items: center;
    gap: 12px;
  }
  .back-brand .brand-dot { background: var(--white); }
  .back-brand .brand-name {
    font-size: 42px;
    font-weight: 700;
    color: var(--white);
  }
  .back-rule {
    position: absolute;
    left: 150px; right: 150px;
    top: 170px;
    height: 1px;
    background: rgba(255,255,255,0.8);
  }
  .tagline {
    position: absolute;
    left: 0; right: 0;
    top: 186px;
    text-align: center;
    font-size: 10.5px;
    font-weight: 500;
    letter-spacing: 0.8px;
    line-height: 16px;
    text-transform: uppercase;
  }
</style>
</head>
<body>
  <section class="card card-front" aria-label="Card front">
    <div class="front-brand">
      <span class="brand-dot"></span>
      <span class="brand-name">Lumivela</span>
    </div>
    <div class="divider"></div>
    <div class="contact-block">
      <p class="person-name">Marisa Delacourt BSc.Pharm</p>
      <p class="person-title">CERTIFIED VELMORA® INJECTOR</p>
      <div class="contact-row">
        <svg width="10" height="14" viewBox="0 0 10 14" aria-hidden="true"><rect x="1" y="0.8" width="8" height="12.4" rx="1.5" fill="none" stroke="#2a2a2a" stroke-width="1.3"/><line x1="4" y1="11" x2="6" y2="11" stroke="#2a2a2a" stroke-width="1.2"/></svg>
        <span>431 662 0974</span>
      </div>
      <div class="contact-row">
        <svg width="14" height="11" viewBox="0 0 14 11" aria-hidden="true"><rect x="0.7" y="0.7" width="12.6" height="9.6" fill="none" stroke="#2a2a2a" stroke-width="1.2"/><polyline points="0.7,0.7 7,6 13.3,0.7" fill="none" stroke="#2a2a2a" stroke-width="1.2"/></svg>
        <span>marisa@lumivela-example.com</span>
      </div>
      <div class="contact-row">
        <svg width="12" height="15" viewBox="0 0 12 15" aria-hidden="true"><path d="M6 14 C6 14 1 8.5 1 5.5 A5 5 0 0 1 11 5.5 C11 8.5 6 14 6 14 Z" fill="none" stroke="#2a2a2a" stroke-width="1.2"/><circle cx="6" cy="5.5" r="1.8" fill="#2a2a2a"/></svg>
        <span>14, 415 Carrow Ridge Road<br>Marrowfield, Northvale<br>K2P 7W3</span>
      </div>
    </div>
  </section>

  <section class="card card-back" aria-label="Card back">
    <div class="back-brand">
      <span class="brand-dot"></span>
      <span class="brand-name">Lumivela</span>
    </div>
    <div class="back-rule"></div>
    <p class="tagline">Anti-aging consultants and cosmetic injectables<br>Located inside the Wayfarer Care Group</p>
  </section>
</body>
</html>
```